Calendar Design Project: 2025 with Specific Edits

This is a straightforward project where your creativity can shine!
Simply take the existing 2024 calendar and adapt it for 2025 by incorporating the new photos I've attached.
Please keep the overall concept of the 2024 calendar intact—your focus will be on enhancing it with fresh visuals.

I can't wait to see your amazing designs!
I am looking for a talented graphic designer to create a new 2025 calendar with specific adjustments.
Pictures attached.
Requirements:
Calendar Size: 52cm x 34cm
March Folder:
Adjust the image named "attached - DJI-0025" to make the circular road darker to match the rest of the design.
May Folder:
Modify the circled area in the May image to ensure it looks consistent with the other road (reference file: "attached - After").
November Folder:
Clear out the circled area in the November image (reference file: "attached - After1").
Please let me know if you have any questions or need further clarification.
I added to my breif a design i made last year for same client.
2025, calendar should be vertical and not horizontal. and some of the photos attache are "Before" and "After" please include together inside each month of the calendar.
Thank you!
Feel free to adjust any details as necessary!

Rumel Tassik

Hello talented designers!

I’m excited to share that this is my 14th project on the PixelHarbor platform, and I’ve been fortunate to have successful collaborations in the past. I'm looking forward to creating a new 2025 calendar with your help, and I believe that with your creativity and skills, we can make this project a success as well!

I hope to establish a long-term relationship with a talented team like yours. As an added incentive, I will be offering a bonus for the winner, and I may select more than one winner, so everyone has a chance to shine!

Let’s make something amazing together!

Best
Update:
cancel or before, only place the After picture

Requirements
Must have
• Project Overview Objective: Create a 2025 calendar using the provided images, maintaining the design concept from the 2024 calendar but enhancing it with new visuals. Format: Vertical layout (52cm x 34cm).

```html
<!DOCTYPE html>
<html lang="en">
<head>
<meta charset="utf-8">
<title>Verda 2025 Calendar – November</title>
<link rel="stylesheet" href="https://fonts.googleapis.com/css2?family=Roboto:wght@400;500;700&family=Open+Sans:wght@600;700&family=Oswald:wght@300;400&display=swap">
<style>
:root{
  --green-bright:#8dc63f;
  --green-brand:#2bb673;
  --green-deep:#1d7a3a;
  --cell-weekend:#c9e6c3;
  --cell-weekday:#ececec;
  --ink:#231f20;
  --ink-soft:#555;
  --paper:#ffffff;
  --photo-light:#b9bcbd;
  --photo-dark:#7d8283;
}
*{margin:0;padding:0;box-sizing:border-box}
html,body{width:785px;height:1200px;overflow:hidden;background:var(--paper)}
.sheet{position:relative;width:785px;height:1200px;overflow:hidden;background:var(--paper);font-family:"Open Sans",sans-serif;color:var(--ink)}
.waves,.photo{position:absolute;left:0;top:0;width:785px;height:1200px}
.brand{position:absolute;left:56px;top:62px}
.brand-name{font-family:"Roboto",sans-serif;font-weight:700;font-size:68px;letter-spacing:2px;line-height:1;color:var(--ink);display:flex;align-items:center;gap:10px}
.brand-name .mark{width:14px;height:14px;background:var(--green-brand)}
.brand-tagline{font-family:"Roboto",sans-serif;font-size:10.5px;color:var(--ink);margin-top:8px;letter-spacing:-.1px}
.year-block{position:absolute;left:42px;top:590px;font-family:"Roboto",sans-serif}
.year-label{font-size:31px;color:var(--green-brand);line-height:1;letter-spacing:-.5px}
.year-number{font-size:70px;font-weight:500;line-height:1;margin-top:2px;letter-spacing:-2px;color:var(--ink)}
.month-title{position:absolute;left:280px;top:645px;font-family:"Roboto",sans-serif;font-size:44px;color:var(--ink-soft);letter-spacing:-1.5px;line-height:1}
.month-grid{position:absolute;left:37px;top:706px;display:grid;grid-template-columns:repeat(7,67px);grid-template-rows:38px repeat(5,48.5px);column-gap:3.6px;row-gap:10.5px}
.month-grid .head{display:flex;align-items:center;justify-content:center;font-size:9px;font-weight:600;background:var(--cell-weekday);color:var(--ink)}
.month-grid .head.weekend{background:var(--cell-weekend);color:var(--green-deep)}
.month-grid .day{position:relative;background:var(--cell-weekday);font-weight:700;font-size:22px;display:flex;align-items:flex-end;padding:0 0 3px 3px;line-height:1}
.month-grid .day.weekend{background:var(--cell-weekend);color:var(--green-deep)}
.day.split{overflow:hidden}
.day.split svg{position:absolute;inset:0;width:100%;height:100%}
.day.split .upper{position:absolute;right:4px;top:5px}
.mini{position:absolute;left:568px;width:184px;font-family:"Roboto",sans-serif}
.mini-title{font-size:14px;letter-spacing:-.4px;line-height:1;display:flex;align-items:center;gap:5px;padding-left:4px;color:var(--ink)}
.mini-title .sep{width:1.5px;height:15px;background:#aaa}
.mini-title .yr{color:var(--green-brand)}
.mini-grid{display:grid;grid-template-columns:repeat(7,24.6px);column-gap:1.6px;row-gap:4px;margin-top:7px;font-family:"Open Sans",sans-serif}
.mini-grid .head{height:15px;font-size:3.6px;display:flex;align-items:center;justify-content:center;background:var(--cell-weekday);margin-bottom:-2px}
.mini-grid .head.weekend{background:var(--cell-weekend);color:var(--green-deep)}
.mini-grid .d{height:18px;font-size:8px;font-weight:600;display:flex;align-items:flex-end;padding:0 0 2px 4px;background:var(--cell-weekday)}
.mini-grid .d.weekend{background:var(--cell-weekend);color:var(--green-deep)}
.mini-grid .d.blank{background:var(--paper)}
.mini-grid .d.blank.weekend{background:var(--cell-weekend)}
.mini-grid .d.blank.empty{background:var(--cell-weekday)}
.footer{position:absolute;left:38px;top:1063px;width:715px;display:flex;align-items:center;justify-content:space-between;font-family:"Oswald",sans-serif;font-weight:300;font-size:11.3px;color:var(--ink)}
.footer-brand{font-family:"Roboto",sans-serif;width:66px}
.footer-brand .name{font-weight:700;font-size:19px;line-height:1;display:flex;align-items:center;gap:3px}
.footer-brand .name i{width:5px;height:5px;background:var(--green-brand)}
.footer-brand .tag{font-size:3.3px;margin-top:2px;white-space:nowrap}
.footer b{font-weight:400;color:var(--green-brand)}
</style>
</head>
<body>
<main class="sheet">
  <svg class="waves" viewBox="0 0 785 1200" aria-hidden="true">
    <defs>
      <linearGradient id="greenSweep" x1="0" x2="1" y1="0" y2="0">
        <stop offset="0" stop-color="#ffffff"/>
        <stop offset=".45" stop-color="#d6ecb4"/>
        <stop offset=".8" stop-color="#8dc63f"/>
        <stop offset="1" stop-color="#b8dc86"/>
      </linearGradient>
      <linearGradient id="greenLow" x1="0" x2="1" y1="0" y2="0">
        <stop offset="0" stop-color="#ffffff"/>
        <stop offset=".35" stop-color="#cfe8a5"/>
        <stop offset=".85" stop-color="#8dc63f"/>
        <stop offset="1" stop-color="#a6d26a"/>
      </linearGradient>
    </defs>
    <path d="M0 0 H785 V105 C620 70 520 95 430 120 C300 155 150 190 0 186 Z" fill="url(#greenSweep)"/>
    <path d="M0 0 H460 C330 30 180 40 0 20 Z" fill="#ffffff" opacity=".85"/>
    <path d="M0 535 C180 495 330 520 470 522 C620 524 700 480 785 458 V633 C700 640 600 620 470 610 C300 598 160 565 0 570 Z" fill="url(#greenLow)"/>
  </svg>

  <svg class="photo" viewBox="0 0 785 1200" role="img" aria-label="Photo of a newly paved interlocking-brick estate road with white lane markings, striped kerbs and a concrete company sign beside a white boundary wall">
    <defs>
      <linearGradient id="roadTone" x1="0" x2="0" y1="0" y2="1">
        <stop offset="0" stop-color="#dfe2e3"/>
        <stop offset=".35" stop-color="#a3a7a8"/>
        <stop offset="1" stop-color="#7d8283"/>
      </linearGradient>
    </defs>
    <path d="M0 170 C150 185 300 150 440 118 C560 92 680 82 785 88 V458 C700 480 620 524 470 522 C330 520 180 495 0 535 Z" fill="url(#roadTone)"/>
  </svg>

  <header class="brand">
    <div class="brand-name"><span class="mark"></span>VERDA</div>
    <div class="brand-tagline">VERDA ROADS &amp; CIVIL WORKS</div>
  </header>

  <section class="year-block">
    <div class="year-label">CALENDAR</div>
    <div class="year-number">2025</div>
  </section>
  <h1 class="month-title">NOVEMBER</h1>

  <section class="month-grid">
    <div class="head weekend">SUNDAY</div><div class="head">MONDAY</div><div class="head">TUESDAY</div><div class="head">WEDNESDAY</div><div class="head">THURSDAY</div><div class="head">FRIDAY</div><div class="head weekend">SATURDAY</div>
    <div class="day weekend"></div><div class="day"></div><div class="day"></div><div class="day"></div><div class="day"></div><div class="day"></div><div class="day weekend">1</div>
    <div class="day weekend">2</div><div class="day">3</div><div class="day">4</div><div class="day">5</div><div class="day">6</div><div class="day">7</div><div class="day weekend">8</div>
    <div class="day weekend">9</div><div class="day">10</div><div class="day">11</div><div class="day">12</div><div class="day">13</div><div class="day">14</div><div class="day weekend">15</div>
    <div class="day weekend">16</div><div class="day">17</div><div class="day">18</div><div class="day">19</div><div class="day">20</div><div class="day">21</div><div class="day weekend">22</div>
    <div class="day weekend split"><svg viewBox="0 0 67 48.5" preserveAspectRatio="none" aria-hidden="true"><line x1="0" y1="0" x2="67" y2="48.5" stroke="#fff" stroke-width="1"/></svg><span class="upper">30</span>23</div><div class="day">24</div><div class="day">25</div><div class="day">26</div><div class="day">27</div><div class="day">28</div><div class="day weekend">29</div>
  </section>

  <section class="mini" style="top:704px">
    <div class="mini-title">OCTOBER<span class="sep"></span><span class="yr">2025</span></div>
    <div class="mini-grid">
      <div class="head weekend">SUNDAY</div><div class="head">MONDAY</div><div class="head">TUESDAY</div><div class="head">WEDNESDAY</div><div class="head">THURSDAY</div><div class="head">FRIDAY</div><div class="head weekend">SATURDAY</div>
      <div class="d blank weekend"></div><div class="d blank empty"></div><div class="d blank empty"></div><div class="d">1</div><div class="d">2</div><div class="d">3</div><div class="d weekend">4</div>
      <div class="d weekend">5</div><div class="d">6</div><div class="d">7</div><div class="d">8</div><div class="d">9</div><div class="d">10</div><div class="d weekend">11</div>
      <div class="d weekend">12</div><div class="d">13</div><div class="d">14</div><div class="d">15</div><div class="d">16</div><div class="d">17</div><div class="d weekend">18</div>
      <div class="d weekend">19</div><div class="d">20</div><div class="d">21</div><div class="d">22</div><div class="d">23</div><div class="d">24</div><div class="d weekend">25</div>
      <div class="d weekend">26</div><div class="d">27</div><div class="d">28</div><div class="d">29</div><div class="d">30</div><div class="d">31</div><div class="d blank weekend"></div>
    </div>
  </section>

  <section class="mini" style="top:893px">
    <div class="mini-title">DECEMBER<span class="sep"></span><span class="yr">2025</span></div>
    <div class="mini-grid">
      <div class="head weekend">SUNDAY</div><div class="head">MONDAY</div><div class="head">TUESDAY</div><div class="head">WEDNESDAY</div><div class="head">THURSDAY</div><div class="head">FRIDAY</div><div class="head weekend">SATURDAY</div>
      <div class="d blank weekend"></div><div class="d">1</div><div class="d">2</div><div class="d">3</div><div class="d">4</div><div class="d">5</div><div class="d weekend">6</div>
      <div class="d weekend">7</div><div class="d">8</div><div class="d">9</div><div class="d">10</div><div class="d">11</div><div class="d">12</div><div class="d weekend">13</div>
      <div class="d weekend">14</div><div class="d">15</div><div class="d">16</div><div class="d">17</div><div class="d">18</div><div class="d">19</div><div class="d weekend">20</div>
      <div class="d weekend">21</div><div class="d">22</div><div class="d">23</div><div class="d">24</div><div class="d">25</div><div class="d">26</div><div class="d weekend">27</div>
      <div class="d weekend">28</div><div class="d">29</div><div class="d">30</div><div class="d">31</div><div class="d blank empty"></div><div class="d blank empty"></div><div class="d blank weekend"></div>
    </div>
  </section>

  <footer class="footer">
    <div class="footer-brand"><div class="name"><i></i>VERDA</div><div class="tag">VERDA ROADS &amp; CIVIL WORKS</div></div>
    <span><b>T</b>: +234 800 555 0142</span>
    <span><b>E</b>: hello@verdaworks.example</span>
    <span><b>W</b>: www.verdaworks.example</span>
    <span><b>A</b>: 22 Crestfield Avenue, Suite 4, Greenvale District, Harbor City</span>
  </footer>
</main>
</body>
</html>
```